Hip / Cool Business Card for Custom Accessory Company

I would like to get a 2 sided design for standard size business cards, glossy (2 inches x 3.5 inches). Can be landscape or portrait layout! The design should include our logo (attached). The card should be extremely clear that the company is Tin Lantern. Should also have our URL clear. Should also use the color scheme seen on our upcoming site, tinlantern-example.com. The font we use is called "hurry up." Other than that, please go-to-town. We are targeting 15-45 y.o. market, with a skew on the 20-30 crowd. We do custom and stock iPhone cases as well as Cufflinks, Winestoppers; see the website for more.
Updates

Project Deadline Extended
Reason: Extending in case the US July 4th Holiday is keeping people from working!!

Industry/Entity Type

Landscape

Requirements
Must have
• Must be clear that the website is tinlantern-example.com. Must be clear that custom designs are an option.
Nice to have
• images of our designs. examples of our designs.
Should not have
• hard on the eyes contrasting colors such as orange on black. green on blue. Should not have any fonts that are considered "old" like Times New Roman. But decorative fonts are fine.

```html
<!DOCTYPE html>
<html lang="en">
<head>
<meta charset="UTF-8">
<title>Tin Lantern Business Card</title>
<link rel="stylesheet" href="https://fonts.googleapis.com/css2?family=Freckle+Face&family=Open+Sans:wght@400&display=swap">
<style>
  :root {
    --backdrop: #05565b;
    --card: #ffffff;
    --tab: #e6e6e6;
    --brand: #1a9ba8;
    --ink: #111111;
  }
  html, body {
    margin: 0;
    padding: 0;
    width: 873px;
    height: 1200px;
    overflow: hidden;
    background: var(--backdrop);
  }
  .canvas {
    position: relative;
    width: 873px;
    height: 1200px;
  }
  .card {
    position: absolute;
    left: 39px;
    width: 794px;
    height: 475px;
    background: var(--card);
    border-radius: 20px;
    overflow: hidden;
  }
  .card--front { top: 80px; }
  .card--back { top: 625px; }

  .brand-tab {
    position: absolute;
    left: 0;
    top: 131px;
    width: 217px;
    height: 213px;
    background: var(--tab);
    border-radius: 0 70px 70px 0;
    display: flex;
    flex-direction: column;
    align-items: center;
    justify-content: center;
    gap: 10px;
  }
  .brand-mark {
    border-radius: 50%;
    background: var(--brand);
  }
  .brand-tab .brand-mark { width: 78px; height: 78px; }
  .brand-name {
    font-family: "Freckle Face", "Trebuchet MS", sans-serif;
    color: var(--brand);
    text-transform: uppercase;
    line-height: 1;
    margin: 0;
    font-weight: 400;
  }
  .brand-tab .brand-name { font-size: 28px; }

  .company-title {
    position: absolute;
    left: 277px;
    top: 72px;
    font-size: 64px;
    letter-spacing: 1px;
    white-space: nowrap;
  }

  .contact {
    position: absolute;
    left: 275px;
    margin: 0;
    font-family: "Open Sans", Arial, sans-serif;
  }
  .contact dt {
    position: absolute;
    left: 0;
    top: 3px;
    font-family: "Freckle Face", "Trebuchet MS", sans-serif;
    color: var(--brand);
    font-size: 23px;
    text-transform: uppercase;
    white-space: nowrap;
  }
  .contact dd {
    margin: 0 0 0 136px;
    color: var(--ink);
    font-size: 21px;
    line-height: 31px;
    letter-spacing: 0.3px;
    white-space: nowrap;
  }
  .contact--address { top: 196px; }
  .contact--email { top: 290px; }
  .contact--web { top: 342px; }

  .back-lockup {
    position: absolute;
    inset: 0;
    display: flex;
    flex-direction: column;
    align-items: center;
    justify-content: center;
    gap: 22px;
  }
  .back-lockup .brand-mark { width: 170px; height: 170px; }
  .back-lockup .brand-name { font-size: 62px; }
  .tagline {
    margin: 0;
    font-family: "Open Sans", Arial, sans-serif;
    font-size: 20px;
    color: var(--ink);
    letter-spacing: 0.3px;
  }
</style>
</head>
<body>
<main class="canvas">
  <section class="card card--front" aria-label="Card front">
    <div class="brand-tab">
      <span class="brand-mark" aria-hidden="true"></span>
      <p class="brand-name">Tin Lantern</p>
    </div>
    <h1 class="brand-name company-title">Tin Lantern</h1>
    <dl class="contact contact--address">
      <dt>Address -</dt>
      <dd>418B Cedar Ridge Lane<br>Unit 207 Fairview, OR 97024</dd>
    </dl>
    <dl class="contact contact--email">
      <dt>E Mail -</dt>
      <dd>support@tinlantern-example.com</dd>
    </dl>
    <dl class="contact contact--web">
      <dt>Web -</dt>
      <dd>tinlantern-example.com</dd>
    </dl>
  </section>

  <section class="card card--back" aria-label="Card back">
    <div class="back-lockup">
      <span class="brand-mark" aria-hidden="true"></span>
      <p class="brand-name">Tin Lantern</p>
      <p class="tagline">Custom designs &amp; stock accessories · tinlantern-example.com</p>
    </div>
  </section>
</main>
</body>
</html>
```